Lantern Square, Steady Course. (Website Design)

We are launching a new bipartisan civic movement: Lantern Square. Steady Course.
The mission is this: Americans deserve a government that is legally required to serve them honestly.
We are looking for a world-class website designer capable of creating an emotionally powerful, modern, cinematic landing page experience that feels larger than politics.
This is not a campaign website for a political party or candidate. We are not looking for a red, white, and blue page with stripes, or American flags, or stock footage of smiling people in a voting booth. We are looking for an emotional and cinematic experience through and through.
The visual direction should feel:
Historic
Hopeful
American
Emotional
Cinematic
Trustworthy
Timeless
The goal is to make visitors feel that they are witnessing the beginning of something important and want to be part of it in the end.
Primary Objective:
Inspire visitors to participate in a one-minute survey and cast their vote.
The survey itself is extremely short and takes approximately one minute to complete.
Everything on the page should ultimately guide visitors toward this action while creating enough curiosity, trust, emotional engagement, and excitement that they feel compelled to take part in the movement.
Audience:
The audience is ordinary Americans across the political spectrum: Democrats, Republicans, Independents.
The design should feel unifying and welcoming.
It should avoid looking partisan, ideological, activist, or government-issued.
Creative Freedom:
We are intentionally giving designers substantial creative freedom.
We are not looking for someone to simply arrange content into predefined sections.
Instead, we are looking for a designer who can think strategically about user experience and persuasion.
The ideal design is as minimal as possible, but you may always:
Use as many sections as you believe are necessary.
Use as many images as you believe are necessary.
Include storytelling elements.
Include data visualizations.
Include timelines.
Include videos.
Include animations.
Include or exclude sections as you see fit.
Reorganize the flow entirely.
We uploaded some files containing text and section suggestions. You don’t have to use them.
We also uploaded some images to convey the general feel we’re looking for.
We are much more interested in the effectiveness of the overall experience than in any specific layout.
What success looks like:
Think outside the box.
Please do not create another generic political website. We have already explored those approaches.
We are looking for something different.
The winning design will be the one that most effectively guides visitors from curiosity to belief to participation.
When a visitor reaches the end of the experience, they should feel:
This is bigger than politics.
This is something I can support regardless of party.
This feels credible.
This feels hopeful.
I want to be part of this.
Use the survey results, the research findings, the principles, the storytelling, or any other elements you believe will help build trust and inspire participation.
Don't just impress us with flashy visuals. Impress us with a website experience that inspires people to become part of the movement and cast their vote.
The final call-to-action should feel like the natural conclusion of the journey, not a request for engagement.
Our goal is not simply to inform visitors. Our goal is to inspire them to cast their vote.
Prioritize emotional impact, storytelling, clarity, and persuasion over decorative design elements.
Final words:
Design a website experience that successfully inspires visitors to take the survey and cast their vote.
Think like a storyteller, not just a designer.
Thank you for your interest in the project.
Best of luck.

```html
<!DOCTYPE html>
<html lang="en">
<head>
<meta charset="utf-8">
<title>Lantern Square. Steady Course.</title>
<link href="https://fonts.googleapis.com/css2?family=Playfair+Display:ital,wght@0,400;0,500;1,400;1,500&family=Inter:wght@400;500&display=swap" rel="stylesheet">
<style>
:root{
  --cream:#f7f4ee;
  --sand:#efe5d6;
  --stone:#c9c6bf;
  --ink:#1c1b19;
  --muted:#4a4743;
  --gold:#c0914f;
  --gold-soft:#ecd9bd;
  --rule:#cfc9bf;
  --card:#f8f5ef;
}
*{margin:0;padding:0;box-sizing:border-box}
html,body{width:1200px;height:4827px;overflow:hidden}
body{position:relative;background:var(--cream);color:var(--ink);font-family:"Playfair Display",Georgia,serif}
.abs{position:absolute}
.serif{font-family:"Playfair Display",Georgia,serif}
.sans{font-family:"Inter",Arial,sans-serif}
.it{font-style:italic}
.center{text-align:center;left:0;right:0}

.frame-line{position:absolute;top:758px;bottom:0;width:1px;background:var(--rule)}

.hero{position:absolute;left:0;top:0;width:1200px;height:758px;background:radial-gradient(ellipse at 50% 20%,#2a2a28 0%,#151515 55%,#0b0b0b 100%)}
.wordmark{left:75px;top:35px;color:#fff;font-family:"Inter",Arial,sans-serif;font-size:16px;font-weight:400}
.menu{left:1084px;top:41px;width:40px}
.menu span{display:block;height:2px;background:#fff;margin-bottom:8px}
.hero-title{top:128px;color:#fff;font-size:50px;line-height:50px;letter-spacing:-1px}
.hero-shadow{left:240px;top:276px;width:730px;height:385px;background:#3a3835}
.hero-film{left:229px;top:263px;width:729px;height:393px;background:linear-gradient(180deg,#cfcfcf 0%,#9a9a9a 55%,#3d3d3d 100%)}
.play{left:566px;top:430px;width:52px;height:52px}

.band-who{left:75px;top:758px;width:1050px;height:1211px;background:linear-gradient(180deg,var(--cream) 0%,var(--cream) 55%,var(--sand) 100%)}
.eyebrow{font-family:"Inter",Arial,sans-serif;font-size:11px;letter-spacing:6px;color:var(--gold);text-transform:uppercase}
.statement{font-style:italic;font-size:30px;line-height:38px;color:var(--ink);letter-spacing:-.5px}
.rule{height:1px;background:var(--rule)}
.who-photo{left:208px;top:1297px;width:784px;height:372px;background:linear-gradient(90deg,#bfb6aa 0%,#9eaab6 40%,#c89b6a 72%,#3b3f46 100%)}
.h2{font-size:38px;color:var(--ink);letter-spacing:-.5px}
.h2 em{font-style:italic}
.small{font-family:"Inter",Arial,sans-serif;font-size:11px;line-height:19px;color:var(--muted)}

.tl-axis{left:600px;top:2140px;width:1px;height:430px;background:var(--rule)}
.tl-dot{width:14px;height:14px;border:1.5px solid var(--gold);border-radius:50%;background:var(--cream)}
.year{font-size:82px;color:var(--gold);line-height:1}
.tl-text{font-style:italic;font-size:17px;line-height:22px;color:var(--muted);width:360px}

.band-principles{left:75px;top:2700px;width:1050px;height:784px;background:linear-gradient(180deg,var(--cream) 0%,#ecebe6 45%,var(--stone) 100%)}
.card{background:var(--card);padding:32px 46px 32px 34px}
.card.focus{outline:2px dashed #d8d3ca;outline-offset:-6px}
.badge{display:inline-block;background:var(--gold-soft);color:var(--gold);font-family:"Inter",Arial,sans-serif;font-size:13px;padding:7px 24px;margin-bottom:22px}
.badge.solid{background:var(--gold);color:#fff}
.card p{font-size:17px;line-height:22px;color:var(--ink)}

.stat-big{font-size:118px;line-height:1;color:var(--ink)}
.stat-big span{color:var(--gold)}
.row-label{font-family:"Inter",Arial,sans-serif;font-size:13px;color:var(--ink)}
.row-val{font-size:29px;color:var(--ink)}
.bar{height:2px;background:var(--rule)}
.bar i{display:block;height:2px;background:#c9a77a}

.cta-text{font-style:italic;font-size:20px;line-height:28px;color:var(--ink);width:510px;letter-spacing:-.4px}
.cta-link{font-family:"Inter",Arial,sans-serif;font-size:18px;color:var(--gold);letter-spacing:1px}
.cta-btn{background:var(--gold);color:#fff;font-family:"Inter",Arial,sans-serif;font-size:19px;letter-spacing:7px;display:flex;align-items:center;justify-content:center}
.cta-photo{left:690px;top:4213px;width:435px;height:435px;background:linear-gradient(90deg,#5a5a5a 0%,#9c9c9c 45%,#e4e4e4 70%,#cfcfcf 100%)}
.cta-note{left:546px;top:4532px;width:311px;height:64px;background:#ece8e1;font-style:italic;font-size:16px;line-height:20px;color:var(--ink);display:flex;align-items:center;justify-content:center;text-align:center}

.footer{left:75px;top:4712px;width:1050px;height:41px;background:#2b2b2b;color:#fff;font-family:"Inter",Arial,sans-serif;font-size:11px;display:flex;align-items:center;justify-content:center}
</style>
</head>
<body>

<header class="hero">
  <div class="abs wordmark">Lantern Square Collective</div>
  <div class="abs menu" aria-label="Menu"><span></span><span></span></div>
  <h1 class="abs center hero-title serif" style="font-weight:400">Lantern Square<br><em>Steady Course</em></h1>
  <div class="abs hero-shadow"></div>
  <div class="abs hero-film" role="img" aria-label="Film still of a domed capitol building in black and white"></div>
  <svg class="abs play" viewBox="0 0 52 52" aria-label="Play video">
    <circle cx="26" cy="26" r="24" fill="rgba(40,38,34,.7)" stroke="#b08a55" stroke-width="2"/>
    <path d="M21 17 L35 26 L21 35 Z" fill="#fff"/>
  </svg>
</header>

<div class="frame-line" style="left:75px"></div>
<div class="frame-line" style="left:1125px"></div>

<section class="abs band-who"></section>

<section class="mission">
  <div class="abs center eyebrow" style="top:842px">Mission Statement</div>
  <p class="abs center statement" style="top:880px">Today, Not A Single Law Binds Our Government<br>To Act Honestly, And In Our Best Interest.</p>
  <p class="abs center statement" style="top:993px">If Our Government Exists Solely To Serve Us,<br>Why Isn't It Legally Required To?</p>
  <p class="abs center statement" style="top:1105px">We Founded This Movement To Change That.</p>
  <div class="abs rule" style="left:208px;top:1217px;width:784px"></div>
</section>

<section class="who">
  <div class="abs who-photo" role="img" aria-label="A man in a suit reading papers beside his shadow on a stone wall"></div>
  <h2 class="abs center h2" style="top:1700px;font-weight:400">Who <em>We Are</em></h2>
  <p class="abs center small" style="top:1759px">We Are A Bipartisan Movement Based In Washington, D.C.</p>
  <p class="abs center small" style="top:1788px">We Believe Americans Deserve A Government Legally Required To Act Honestly,<br>Transparently, And In The Public's Best Interest.</p>
  <p class="abs center small" style="top:1836px">At A Time Of Growing Division And Distrust, We Are Working To Unite Americans Around A Simple Idea:</p>
  <p class="abs center it" style="top:1872px;font-size:18px;line-height:22px">Government Should Faithfully Serve The People,<br>Not Special Interests.</p>
</section>

<section class="journey">
  <h2 class="abs center h2" style="top:2055px;font-weight:400">Our <em>Journey</em></h2>
  <div class="abs tl-axis"></div>

  <div class="abs year" style="left:358px;top:2143px">2024</div>
  <div class="abs tl-dot" style="left:593px;top:2177px"></div>
  <p class="abs tl-text" style="left:670px;top:2150px">We Started A Nonprofit With This<br>Goal In Mind: Americans Deserve An<br>Honest Government.</p>

  <p class="abs tl-text" style="left:170px;top:2313px;text-align:right">We Identified 10 Principles<br>That Most Of Americans Agree Our<br>Government Must Uphold.</p>
  <div class="abs tl-dot" style="left:593px;top:2340px"></div>
  <div class="abs year" style="left:670px;top:2306px">2025</div>

  <div class="abs year" style="left:358px;top:2469px">2026</div>
  <div class="abs tl-dot" style="left:593px;top:2503px"></div>
  <p class="abs tl-text" style="left:670px;top:2465px;width:380px">We Transformed Those Principles Into Lantern<br>Square, Steady Course — Then Tested It In A<br>Pre-Registered National Study Across The<br>Political Spectrum.</p>

  <div class="abs rule" style="left:208px;top:2649px;width:784px"></div>
</section>

<section class="abs band-principles"></section>
<section class="principles">
  <h2 class="abs center h2" style="top:2752px;font-weight:400">The Seven <em>Principles.</em></h2>

  <div class="abs card" style="left:156px;top:2835px;width:287px;height:203px"><span class="badge">PRINCIPLES 01</span><p>Public Officials Should Serve Only The Public Good. Not Private Interests.</p></div>
  <div class="abs card focus" style="left:456px;top:2835px;width:287px;height:203px"><span class="badge solid">PRINCIPLES 02</span><p>Major Decisions Should Be Based On Truth And Evidence. Not Party Loyalty Or Donors.</p></div>
  <div class="abs card" style="left:756px;top:2835px;width:287px;height:203px"><span class="badge">PRINCIPLES 03</span><p>Government Reasoning Should Be Visible. Clearly. Honestly. On Record.</p></div>

  <div class="abs card" style="left:156px;top:3053px;width:287px;height:202px"><span class="badge">PRINCIPLES 04</span><p>Citizens Should Be Able To Challenge Decisions And Receive Real Responses.</p></div>
  <div class="abs card" style="left:456px;top:3053px;width:287px;height:202px"><span class="badge">PRINCIPLES 05</span><p>Conflicts Of Interest Must Be Disclosed Before Decisions Are Made.</p></div>
  <div class="abs card" style="left:756px;top:3053px;width:287px;height:202px"><span class="badge">PRINCIPLES 06</span><p>Lying Or Misleading The Public In Official Decisions Should Carry Consequences. Real Ones.</p></div>

  <div class="abs card" style="left:287px;top:3270px;width:624px;height:143px;text-align:center;padding:28px 34px"><span class="badge">PRINCIPLES 07</span><p>And Most Importantly, Money Should Never Outweigh People's Voice.<br>89.9%* Said Agree.</p></div>
</section>

<section class="results">
  <div class="abs center eyebrow" style="top:3577px">What Americans Said</div>
  <h2 class="abs center h2" style="top:3600px;font-weight:400">Across Every Line That Divides Us.</h2>

  <div class="abs sans" style="left:202px;top:3711px;font-size:10px;color:var(--gold);letter-spacing:.5px">AGREED WITH THE PRINCIPLES</div>
  <div class="abs stat-big" style="left:200px;top:3722px">89<span>.9%</span></div>
  <p class="abs it" style="left:202px;top:3866px;font-size:17px;line-height:22px;color:var(--muted)">And 82.9% Supported A Legal<br>Framework Built Around Them.</p>

  <div class="abs row-label" style="left:599px;top:3717px">Yes</div>
  <div class="abs row-val" style="right:208px;top:3703px;color:var(--gold)">82.9%</div>
  <div class="abs bar" style="left:596px;top:3746px;width:396px"><i style="width:255px"></i></div>

  <div class="abs row-label" style="left:599px;top:3795px">Neutral</div>
  <div class="abs row-val" style="right:208px;top:3781px">14.4%</div>
  <div class="abs bar" style="left:596px;top:3825px;width:396px"><i style="width:255px"></i></div>

  <div class="abs row-label" style="left:599px;top:3873px">Opposed</div>
  <div class="abs row-val" style="right:208px;top:3859px">2.7%</div>
  <div class="abs bar" style="left:596px;top:3902px;width:396px"><i style="width:255px"></i></div>

  <div class="abs row-label" style="left:599px;top:3936px">By Party · Balanced</div>
  <div class="abs rule" style="left:596px;top:3971px;width:396px"></div>

  <div class="abs row-val" style="left:596px;top:3990px">84.5%</div>
  <div class="abs row-label" style="left:597px;top:4026px">Democrats</div>
  <div class="abs row-val" style="left:748px;top:3990px">80.2%</div>
  <div class="abs row-label" style="left:749px;top:4026px">Republicans</div>
  <div class="abs row-val" style="left:898px;top:3990px">79.9%</div>
  <div class="abs row-label" style="left:899px;top:4026px">Independents</div>

  <div class="abs rule" style="left:208px;top:4125px;width:784px"></div>
</section>

<section class="cta">
  <p class="abs cta-text" style="left:146px;top:4280px">For Decades, We Have Argued Over Policies, Parties, And Ideologies. But Today, Across Political Lines, Generations, And Races, Americans Are Arriving At The Same Conclusion: We Deserve A Government Legally Required To Serve The People Honestly And We Don't Have To Ask For It. We Just Have To Vote For It.</p>
  <div class="abs cta-link" style="left:146px;top:4481px">BE PART OF HISTORY.</div>
  <a class="abs cta-btn" style="left:146px;top:4521px;width:216px;height:34px">VOTE NOW.</a>
  <div class="abs cta-photo" role="img" aria-label="Black and white photo of voters at a polling booth"></div>
  <div class="abs cta-note">1016 People<br>Already Voted YES For The Ballot</div>
</section>

<footer class="abs footer">2026 Lantern Square Collective</footer>

</body>
</html>
```